We are in search of a new business card design for our business. We have a Mexican Grocery Store called Tortilla Grove Market, we would like to see that some have mexican design, but we are open to any type of designs.

Phone: to be announced
Fax: to be announced

Address is:
2415 Calloway Blvd
Dundalk, MD 21222

```html
<!DOCTYPE html>
<html lang="en">
<head>
<meta charset="utf-8">
<title>Tortilla Grove Market – Business Card</title>
<link rel="stylesheet" href="https://fonts.googleapis.com/css2?family=Arimo:wght@400;700&display=swap">
<style>
  :root {
    --backdrop: #5b4a3d;
    --card-white: #ffffff;
    --band-green: #217a00;
    --brand-red: #a3151a;
    --name-red: #8a1f1f;
    --title-orange: #f0840f;
    --body-grey: #555555;
    --label-red: #b01c1c;
    --back-orange: #ff850d;
    --art-warm: #c0501a;
    --art-cool: #7a8a1a;
  }
  html, body {
    margin: 0;
    padding: 0;
    width: 1200px;
    height: 987px;
    overflow: hidden;
    background: var(--backdrop);
    font-family: "Arimo", Arial, sans-serif;
  }
  .canvas {
    position: relative;
    width: 1200px;
    height: 987px;
  }
  .card {
    position: absolute;
    left: 293px;
    width: 615px;
    height: 352px;
  }
  .card-front {
    top: 130px;
    background: var(--card-white);
  }
  .card-back {
    top: 505px;
    background: var(--back-orange);
  }
  .side-band {
    position: absolute;
    left: 25px;
    top: 0;
    width: 84px;
    height: 100%;
    background: var(--band-green);
  }
  .brand-dot {
    position: absolute;
    left: 39px;
    top: 68px;
    width: 56px;
    height: 56px;
    border-radius: 50%;
    background: var(--brand-red);
  }
  .brand-name {
    position: absolute;
    left: 124px;
    top: 62px;
    margin: 0;
    font-weight: 700;
    font-size: 30px;
    line-height: 34px;
    color: var(--brand-red);
  }
  .contact {
    position: absolute;
    right: 30px;
    top: 210px;
    text-align: right;
  }
  .person-name {
    margin: 0;
    font-size: 20px;
    font-weight: 400;
    color: var(--name-red);
    letter-spacing: 0.3px;
  }
  .person-title {
    margin: 3px 0 0;
    font-size: 16px;
    color: var(--title-orange);
  }
  .address {
    margin: 28px 0 0;
    font-size: 15px;
    color: var(--body-grey);
  }
  .phones {
    margin: 8px 0 0;
    font-size: 15px;
    color: var(--body-grey);
  }
  .phones .label {
    color: var(--label-red);
    font-weight: 700;
  }
  .phones .gap { margin-left: 8px; }
  .back-art {
    position: absolute;
    left: 102px;
    top: 96px;
    width: 405px;
    height: 147px;
    background: linear-gradient(90deg, var(--art-warm) 0%, var(--art-cool) 100%);
  }
  .website {
    position: absolute;
    left: 0;
    width: 100%;
    top: 300px;
    text-align: center;
    font-size: 14px;
    letter-spacing: 4px;
    color: var(--card-white);
    margin: 0;
  }
</style>
</head>
<body>
<main class="canvas">
  <section class="card card-front">
    <div class="side-band"></div>
    <div class="brand-dot"></div>
    <h1 class="brand-name">Tortilla Grove<br>Market</h1>
    <div class="contact">
      <h2 class="person-name">MARCO RUIZ</h2>
      <p class="person-title">President</p>
      <p class="address">2415 Calloway Blvd, Dundalk, MD 21222</p>
      <p class="phones"><span class="label">P :</span> 410 555 0147 <span class="label gap">F :</span> 410 555 0182</p>
    </div>
  </section>
  <section class="card card-back">
    <div class="back-art" role="img" aria-label="Illustration area: a red and a green chili pepper"></div>
    <p class="website">www.tortillagrove.com</p>
  </section>
</main>
</body>
</html>
```